Brindle cards

I am in the auto motive, transportation business I would like a business card that is Something cool, modern edgy, having to do with car culture. I offer towing service for high and exotic cars. I also provide towing for collisions and car accidents. I offer open and enclosed transport nationwide.

Target Market(s)

Car culture people high end auto collectors

Industry/Entity Type

Towing car carrier

Contact Information for Business Card

My company colors black yellow and silver

Font styles to use
Serif

```html
<!DOCTYPE html>
<html lang="en">
<head>
<meta charset="utf-8">
<title>Brindle Cards</title>
<link rel="stylesheet" href="https://fonts.googleapis.com/css2?family=Arvo:wght@400;700&family=Lato:wght@400&display=swap">
<style>
  :root {
    --backdrop: #141414;
    --silver-light: #e6e9ee;
    --silver-mid: #b4bac3;
    --silver-dark: #8b929c;
    --brand-yellow: #f9e05c;
    --ink: #0c0c0c;
  }
  * { box-sizing: border-box; margin: 0; padding: 0; }
  html, body { width: 1200px; height: 1122px; overflow: hidden; background: var(--backdrop); }
  .sheet {
    position: relative;
    width: 1200px;
    height: 1122px;
    display: flex;
    flex-direction: column;
    align-items: center;
    justify-content: center;
    gap: 44px;
  }
  .card {
    position: relative;
    width: 800px;
    height: 457px;
    border-radius: 28px;
    overflow: hidden;
  }
  .card--front {
    background: linear-gradient(100deg, var(--silver-dark) 0%, var(--silver-mid) 25%, var(--silver-light) 50%, var(--silver-mid) 75%, var(--silver-dark) 100%);
    display: flex;
    align-items: center;
    justify-content: center;
  }
  .brand {
    display: flex;
    align-items: center;
    gap: 18px;
  }
  .brand__dot {
    width: 38px;
    height: 38px;
    border-radius: 50%;
    background: var(--brand-yellow);
  }
  .brand__name {
    font-family: "Arvo", serif;
    font-weight: 700;
    font-size: 84px;
    letter-spacing: 2px;
    color: var(--ink);
    text-transform: uppercase;
  }
  .card--back { background: var(--brand-yellow); color: var(--ink); }
  .truck-art {
    position: absolute;
    left: 110px;
    top: 48px;
    width: 690px;
    height: 220px;
    border-radius: 14px 0 60px 30px;
    background: linear-gradient(90deg, #111 0%, #1d1d1d 55%, rgba(20,20,20,0.55) 100%);
  }
  .person {
    position: absolute;
    left: 56px;
    bottom: 52px;
  }
  .person__name {
    font-family: "Arvo", serif;
    font-weight: 400;
    font-size: 36px;
    letter-spacing: 1px;
    text-transform: uppercase;
    line-height: 1.1;
  }
  .person__role {
    font-family: "Lato", sans-serif;
    font-size: 22px;
    margin-top: 4px;
  }
  .contact {
    position: absolute;
    right: 48px;
    bottom: 66px;
    list-style: none;
    font-family: "Lato", sans-serif;
    text-align: right;
  }
  .contact__item {
    display: flex;
    align-items: center;
    justify-content: flex-end;
    gap: 10px;
    font-size: 17px;
    line-height: 1.55;
  }
  .contact__item--phone { font-size: 25px; }
  .contact__icon { width: 15px; height: 15px; fill: var(--ink); flex: none; }
</style>
</head>
<body>
<main class="sheet">
  <section class="card card--front" aria-label="Card front">
    <div class="brand">
      <span class="brand__dot"></span>
      <span class="brand__name">Brindle</span>
    </div>
  </section>

  <section class="card card--back" aria-label="Card back">
    <div class="truck-art" role="img" aria-label="Large black silhouette illustration of a flatbed tow truck"></div>
    <div class="person">
      <p class="person__name">Dean Callaway</p>
      <p class="person__role">Managing Director</p>
    </div>
    <ul class="contact">
      <li class="contact__item contact__item--phone">123-456-7890
        <svg class="contact__icon" viewBox="0 0 24 24"><path d="M6.6 10.8a15.1 15.1 0 0 0 6.6 6.6l2.2-2.2a1 1 0 0 1 1-.25 11.4 11.4 0 0 0 3.6.57 1 1 0 0 1 1 1V20a1 1 0 0 1-1 1A17 17 0 0 1 3 4a1 1 0 0 1 1-1h3.5a1 1 0 0 1 1 1c0 1.25.2 2.45.57 3.57a1 1 0 0 1-.25 1z"/></svg>
      </li>
      <li class="contact__item">callaway@yourwebsite.com
        <svg class="contact__icon" viewBox="0 0 24 24"><path d="M2 5h20v14H2z M2 5l10 8 10-8" fill="none" stroke="#0c0c0c" stroke-width="2"/></svg>
      </li>
      <li class="contact__item">www.yourwebsite.com
        <svg class="contact__icon" viewBox="0 0 24 24"><circle cx="12" cy="12" r="9" fill="none" stroke="#0c0c0c" stroke-width="2"/><path d="M3 12h18M12 3c3 3 3 15 0 18M12 3c-3 3-3 15 0 18" fill="none" stroke="#0c0c0c" stroke-width="1.6"/></svg>
      </li>
    </ul>
  </section>
</main>
</body>
</html>
```